Tad Virelli Days on Market

Hello!

We are a dynamic real estate company based in Noraville, Australia and we are looking to freshen up our days on market brochure. We would like to update the style as well as the content (details of sold properties (June-Dec 2014) attached in excel doc along with updated track record data). I have attached the last one we did for reference (Jan-Jul 2014). The brochure is used in both print and PDF format and needs to be clear, concise and easily read. Please ensure company logo, details (address/phone/website etc), staff photo and company colours are used. Our company motto is Done. Different. so if you can include that somewhere we'd be most grateful.

Any queries please shout. Best of luck!

Cheers,

Pim

Industry/Entity Type

Real Estate

```html
<!DOCTYPE html>
<html lang="en">
<head>
<meta charset="utf-8">
<title>Tad Virelli – Days on Market</title>
<link href="https://fonts.googleapis.com/css2?family=Open+Sans:wght@400;600;700&display=swap" rel="stylesheet">
<style>
:root{
  --backdrop:#d9d9d9;
  --paper:#f7f8f8;
  --brand:#2b7fa6;
  --brand-dark:#1b5f80;
  --navy:#0f4a63;
  --ink:#1d2226;
  --muted:#6b7780;
  --table-head:#b9c6d2;
  --photo:#8e9499;
}
*{box-sizing:border-box;margin:0;padding:0}
html,body{width:1200px;height:789px;overflow:hidden}
body{background:var(--backdrop);font-family:"Open Sans",sans-serif;color:var(--ink)}
.brochure{position:absolute;left:330px;top:12px;width:540px;height:764px;background:var(--paper);box-shadow:0 4px 18px rgba(0,0,0,.18);overflow:hidden}
.masthead{position:absolute;left:0;top:0;width:100%;height:92px;display:flex}
.masthead-brand{width:58%;background:var(--brand);display:flex;align-items:flex-end;padding:0 0 14px 24px}
.company-name{font-size:30px;font-weight:400;color:#e6eef3;letter-spacing:1px;text-transform:uppercase}
.masthead-contact{flex:1;background:var(--brand-dark);color:#dbe7ee;font-size:7px;padding:14px 18px 0 0;text-align:right;line-height:1.6}
.agent-photo{position:absolute;left:186px;top:92px;width:118px;height:96px;background:linear-gradient(180deg,#b4b8bb,var(--photo) 60%,#3a3f44)}
.agent-card{position:absolute;left:316px;top:98px;font-size:7px;line-height:1.55;color:var(--muted)}
.agent-card .agent-name{font-weight:700;color:var(--ink);font-size:8px}
.stats{position:absolute;left:0;top:110px;width:180px;text-align:center}
.stat{margin-bottom:34px}
.stat svg{display:block;margin:0 auto 4px}
.stat-label{font-size:11px;line-height:1.15;color:var(--ink)}
.stat-value{font-size:17px;font-weight:700;margin-top:2px}
.stat-first .stat-label{font-size:8px;color:var(--muted)}
.stat-first .stat-value{font-size:11px;color:var(--muted)}
.sales-table{position:absolute;left:186px;top:176px;width:334px;border-collapse:collapse;font-size:7.6px}
.sales-table th{background:var(--table-head);color:#fff;font-weight:600;text-align:left;padding:3px 4px;height:16px}
.sales-table td{padding:0 4px;height:13.5px;white-space:nowrap}
.sales-table td.num,.sales-table th.num{text-align:right}
.footer-band{position:absolute;left:0;bottom:0;width:100%;height:34px;background:var(--navy);color:#e4eef2;font-size:7.6px;display:flex;align-items:center;justify-content:center;text-align:center;padding:0 20px}
</style>
</head>
<body>
<main class="brochure">
  <header class="masthead">
    <div class="masthead-brand"><span class="company-name">Virelli</span></div>
    <div class="masthead-contact">
      <div>02 4300 1000</div>
      <div>info@virellirealty.com.au</div>
      <div>12 Pellow Road, Noraville NSW</div>
    </div>
  </header>

  <div class="agent-photo" role="img" aria-label="Portrait photo of agent Tad Virelli in a dark suit"></div>
  <div class="agent-card">
    <div class="agent-name">Tad Virelli</div>
    <div>Principal</div>
    <div>M 0400 123 456</div>
    <div>P 02 4300 1000</div>
    <div>tad@virellirealty.com.au</div>
  </div>

  <section class="stats">
    <div class="stat stat-first">
      <svg width="34" height="30" viewBox="0 0 34 30"><path d="M3 14 17 3l14 11" fill="none" stroke="#7aa8c0" stroke-width="2.5"/><rect x="8" y="13" width="18" height="14" fill="none" stroke="#7aa8c0" stroke-width="2.5"/><rect x="14" y="18" width="6" height="9" fill="#7aa8c0"/></svg>
      <div class="stat-label">Properties sold in the<br>last six months</div>
      <div class="stat-value">46</div>
    </div>
    <div class="stat">
      <svg width="46" height="34" viewBox="0 0 46 34"><path d="M3 17 23 3l20 14" fill="none" stroke="#1f4e6b" stroke-width="3"/><rect x="10" y="16" width="26" height="16" fill="none" stroke="#1f4e6b" stroke-width="3"/><rect x="13" y="9" width="20" height="10" fill="#fff" stroke="#1f4e6b" stroke-width="2"/><rect x="20" y="24" width="6" height="8" fill="#1f4e6b"/></svg>
      <div class="stat-label">Average Days<br>on Market</div>
      <div class="stat-value">16</div>
    </div>
    <div class="stat">
      <svg width="46" height="34" viewBox="0 0 46 34"><path d="M3 17 23 3l20 14" fill="none" stroke="#1f4e6b" stroke-width="3"/><rect x="10" y="16" width="26" height="16" fill="none" stroke="#1f4e6b" stroke-width="3"/><text x="23" y="29" font-size="12" font-weight="700" text-anchor="middle" fill="#1f4e6b" font-family="Open Sans, sans-serif">$</text></svg>
      <div class="stat-label">Average Sale Price</div>
      <div class="stat-value">$452,863</div>
    </div>
    <div class="stat">
      <svg width="50" height="34" viewBox="0 0 50 34"><rect x="10" y="6" width="16" height="9" rx="1" fill="#1f4e6b" transform="rotate(-20 18 10)"/><rect x="22" y="11" width="24" height="3.5" fill="#1f4e6b" transform="rotate(-20 22 12)"/><rect x="6" y="26" width="20" height="5" fill="#1f4e6b"/></svg>
      <div class="stat-label">Total Sales<br>Transactions</div>
      <div class="stat-value">$19,473,100</div>
    </div>
    <div class="stat">
      <svg width="40" height="38" viewBox="0 0 40 38"><circle cx="20" cy="10" r="8" fill="#1f4e6b"/><path d="M4 37c0-10 7-16 16-16s16 6 16 16z" fill="#1f4e6b"/><circle cx="24" cy="26" r="6" fill="#fff" stroke="#1f4e6b" stroke-width="2.5"/><path d="M19 31l-5 5" stroke="#fff" stroke-width="3"/></svg>
      <div class="stat-label">Total Number of<br>Groups Inspected</div>
      <div class="stat-value">594</div>
    </div>
  </section>

  <table class="sales-table">
    <thead><tr><th>Property</th><th>Sold</th><th class="num">Days</th><th class="num">Price</th><th class="num">Groups</th></tr></thead>
    <tbody>
      <tr><td>51 Quorra Street, Gorokan</td><td>02.07.14</td><td class="num">Off Plan</td><td class="num">$380 000</td><td class="num">4</td></tr>
      <tr><td>7 Tindal Place, Wyong</td><td>07.07.14</td><td class="num">4</td><td class="num">$390 000</td><td class="num">12</td></tr>
      <tr><td>7 Marrow Circuit, Norah Head</td><td>14.07.14</td><td class="num">24</td><td class="num">$465 000</td><td class="num">14</td></tr>
      <tr><td>10 Pellow Road, Noraville</td><td>14.07.14</td><td class="num">12</td><td class="num">$510 000</td><td class="num">9</td></tr>
      <tr><td>31 Yarrock Road, Norah Head</td><td>21.07.14</td><td class="num">8</td><td class="num">$445 000</td><td class="num">10</td></tr>
      <tr><td>29 Ostley Crescent, Gorokan</td><td>23.07.14</td><td class="num">15</td><td class="num">$418 000</td><td class="num">13</td></tr>
      <tr><td>17 Brenlow Drive, Lake Munmorah</td><td>25.07.14</td><td class="num">6</td><td class="num">$545 000</td><td class="num">8</td></tr>
      <tr><td>406 Caddell Road, Tuggerawong</td><td>01.08.14</td><td class="num">18</td><td class="num">$335 000</td><td class="num">15</td></tr>
      <tr><td>22 Hallam Street, Gorokan</td><td>06.08.14</td><td class="num">12</td><td class="num">$349 000</td><td class="num">11</td></tr>
      <tr><td>4 Fenwick Street, Hamlyn Terrace</td><td>11.08.14</td><td class="num">9</td><td class="num">$479 000</td><td class="num">7</td></tr>
      <tr><td>3/17-19 Lunette Place, Woongarrah</td><td>15.08.14</td><td class="num">21</td><td class="num">$405 000</td><td class="num">12</td></tr>
      <tr><td>76 Orrin Road, Woongarrah</td><td>22.08.14</td><td class="num">14</td><td class="num">$498 000</td><td class="num">18</td></tr>
      <tr><td>5 Quenby Close, Lake Haven</td><td>25.08.14</td><td class="num">7</td><td class="num">$371 000</td><td class="num">9</td></tr>
      <tr><td>9 Sarrow Place, Woongarrah</td><td>29.08.14</td><td class="num">28</td><td class="num">$510 000</td><td class="num">14</td></tr>
      <tr><td>25 Delwyn Drive, Kanwal</td><td>30.08.14</td><td class="num">12</td><td class="num">$350 000</td><td class="num">10</td></tr>
      <tr><td>43 Pelham Close, Lake Haven</td><td>02.09.14</td><td class="num">5</td><td class="num">$455 000</td><td class="num">8</td></tr>
      <tr><td>11 Varrick Avenue, San Remo</td><td>09.09.14</td><td class="num">16</td><td class="num">$365 000</td><td class="num">12</td></tr>
      <tr><td>17 Ebbet Road, Gorokan</td><td>12.09.14</td><td class="num">10</td><td class="num">$349 000</td><td class="num">9</td></tr>
      <tr><td>33 Cindral Road, Gwandalan</td><td>18.09.14</td><td class="num">22</td><td class="num">$559 000</td><td class="num">16</td></tr>
      <tr><td>29 Larkspur Cres, Lake Munmorah</td><td>26.09.14</td><td class="num">13</td><td class="num">$411 000</td><td class="num">11</td></tr>
      <tr><td>95 Torvan Road, Summerland Point</td><td>03.10.14</td><td class="num">9</td><td class="num">$610 000</td><td class="num">14</td></tr>
      <tr><td>62 Elvey Avenue, Kanwal</td><td>10.10.14</td><td class="num">31</td><td class="num">$395 000</td><td class="num">19</td></tr>
      <tr><td>11 Brisk Road, Noraville</td><td>16.10.14</td><td class="num">6</td><td class="num">$460 000</td><td class="num">7</td></tr>
      <tr><td>70 Ambery Road, Noraville</td><td>20.10.14</td><td class="num">14</td><td class="num">$505 000</td><td class="num">13</td></tr>
      <tr><td>5 Kelso Drive, Lake Haven</td><td>27.10.14</td><td class="num">11</td><td class="num">$372 000</td><td class="num">10</td></tr>
      <tr><td>23 Fennet Close, Lake Munmorah</td><td>03.11.14</td><td class="num">19</td><td class="num">$430 000</td><td class="num">12</td></tr>
      <tr><td>2 Orla Crescent, Noraville</td><td>06.11.14</td><td class="num">8</td><td class="num">$487 000</td><td class="num">9</td></tr>
      <tr><td>22 Wissel Street, Gorokan</td><td>11.11.14</td><td class="num">15</td><td class="num">$351 000</td><td class="num">11</td></tr>
      <tr><td>75 Tamsin Avenue, Lake Haven</td><td>14.11.14</td><td class="num">10</td><td class="num">$398 000</td><td class="num">8</td></tr>
      <tr><td>19 Dorrigal Avenue, Tuggerawong</td><td>18.11.14</td><td class="num">27</td><td class="num">$415 000</td><td class="num">17</td></tr>
      <tr><td>67 Haverly Street, Lake Munmorah</td><td>24.11.14</td><td class="num">12</td><td class="num">$447 000</td><td class="num">10</td></tr>
      <tr><td>16 Pindar Drive, Budgewoi</td><td>28.11.14</td><td class="num">5</td><td class="num">$405 000</td><td class="num">6</td></tr>
      <tr><td>53 Quandel Avenue, Budgewoi</td><td>01.12.14</td><td class="num">22</td><td class="num">$384 000</td><td class="num">14</td></tr>
      <tr><td>38 Sallow Street, Toukley</td><td>05.12.14</td><td class="num">9</td><td class="num">$375 000</td><td class="num">11</td></tr>
      <tr><td>14 Merrin Avenue, Woongarrah</td><td>10.12.14</td><td class="num">Off Plan</td><td class="num">$376 000</td><td class="num">19</td></tr>
    </tbody>
  </table>

  <footer class="footer-band">Each buyer has been qualified and added to our database. They are the first ones to know about our new listings before they are advertised.</footer>
</main>
</body>
</html>
```